Flyer DIN A6 für www.clubfreude-netz.de
Zielgruppe
Unser Firma macht: Affiliate Marketing (Vereine erhalten Provision (Sponsorgeld) vom Onlineeinkauf),
Zielgruppe:
Unternehmer bzw. Unternehmenseinkäufer, Vereinsmitglieder, Fans die ohne Mehrkosten Geld für Ihren befreundeten Verein sponsoren möchten (die im besten Fall gerne+ viel Online einkaufen)
Aufgabenstellung
Format: DIN A6, 4/0 farbig, Farbwelt: blau siehe www.clubfreude-netz.de,
Papier: 250 g Offset Hochglanz
Flyer wird den Vereinen zugesandt die sich bei clubfreude-netz.de angemeldet haben. Sie haben die Möglichkeit sämtliche befreundete Unternehmen, Fans, Vereinsmitglieder diesen Flyer zu geben und damit Werbung für Ihren Verein zu machen. Bzw. von der Website www.clubfreude-netz.de D.h. je mehr Personen über clubfreude-netz.de einkaufen desto mehr bekommt der Verein Geld für die Vereinskasse. FAZIT: Flyer soll zum anmelden auf www.clubfreude-netz.de verführen. Folgende Gedanken sollten geweckt werden: Ja, wunderbar ich helfe Verein X ohne Extrakosten bei jedem Onlineeinkauf
TEXT:
Unterstützen Sie Ihren Sportverein ohne Extrakosten wie? Mit www.clubfreude-netz.de, Melden Sie sich an!

```html
<!DOCTYPE html>
<html lang="de">
<head>
<meta charset="utf-8">
<title>Flyer DIN A6 – clubfreude-netz.de</title>
<link rel="stylesheet" href="https://fonts.googleapis.com/css2?family=Lilita+One&display=swap">
<style>
  :root {
    --backdrop: #d4d6d8;
    --paper: #ffffff;
    --navy: #1f3a78;
    --red: #b3272d;
    --red-dark: #8e1c21;
    --sky: #d3e2f1;
    --sky-mid: #aec8e8;
    --jersey: #86a9d8;
    --jersey-deep: #6a8cc2;
    --shorts: #39465a;
    --field: #5f8c48;
    --grass-light: #7cc243;
    --grass-dark: #3f8f1f;
  }
  * { box-sizing: border-box; margin: 0; padding: 0; }
  html, body {
    width: 1200px; height: 900px; overflow: hidden;
    background: var(--backdrop);
  }
  .flyer {
    position: absolute;
    left: 310px; top: 40px;
    width: 580px; height: 820px;
    background: var(--paper);
    overflow: hidden;
    box-shadow: 0 6px 24px rgba(0,0,0,.18);
    font-family: "Lilita One", "Arial Black", sans-serif;
  }
  .hero-photo {
    position: absolute; left: 0; top: 0;
    width: 100%; height: 392px;
    background:
      radial-gradient(ellipse 60% 40% at 30% 55%, rgba(134,169,216,.9), rgba(134,169,216,0) 70%),
      radial-gradient(ellipse 30% 45% at 82% 50%, rgba(122,158,210,.85), rgba(122,158,210,0) 70%),
      linear-gradient(180deg,
        var(--sky) 0%,
        var(--sky-mid) 22%,
        var(--jersey) 48%,
        var(--jersey-deep) 72%,
        var(--shorts) 90%,
        var(--field) 100%);
  }
  .signup-badge {
    position: absolute; left: 22px; top: 292px;
    width: 138px; height: 138px; border-radius: 50%;
    background: var(--red);
    border: 3px solid var(--paper);
    box-shadow: 0 0 0 2px var(--red-dark), 0 3px 8px rgba(0,0,0,.25);
    color: var(--paper);
    display: flex; align-items: center; justify-content: center;
    text-align: center;
    font-size: 19px; line-height: 1.05; letter-spacing: .5px;
    transform: rotate(-12deg);
  }
  .brand-mark {
    position: absolute; right: 40px; top: 318px;
    padding: 0 22px; height: 70px;
    background: var(--paper);
    display: flex; align-items: center; justify-content: center; gap: 10px;
    color: var(--navy); font-size: 22px; letter-spacing: .5px;
    box-shadow: 0 2px 8px rgba(0,0,0,.2);
  }
  .brand-mark .dot {
    width: 14px; height: 14px; border-radius: 50%; background: var(--navy);
    flex: none;
  }
  .headline {
    position: absolute; left: 46px; top: 470px;
    color: var(--navy);
    font-size: 48px; line-height: 1.14; letter-spacing: 1px;
    font-weight: 400; text-transform: uppercase;
  }
  .headline .accent { color: var(--red); }
  .web-address {
    position: absolute; left: 46px; top: 696px;
    color: var(--navy);
    font-size: 30px; letter-spacing: .5px; text-transform: uppercase;
  }
  .grass {
    position: absolute; left: 0; bottom: 0;
    width: 100%; height: 70px;
  }
</style>
</head>
<body>
  <main class="flyer">
    <div class="hero-photo" role="img" aria-label="Foto: jubelnde Kinder-Fußballmannschaft in hellblauen Trikots mit Pokal und Trainer auf dem Sportplatz vor blauem Himmel"></div>

    <div class="signup-badge">JETZT<br>KOSTENLOS<br>ANMELDEN!</div>

    <div class="brand-mark"><span class="dot"></span>CLUBFREUDE</div>

    <h1 class="headline">
      Unterstützen<br>
      Sie <span class="accent">Ihren Verein</span><br>
      ohne Extrakosten
    </h1>

    <p class="web-address">www.clubfreude-netz.de</p>

    <svg class="grass" viewBox="0 0 580 70" preserveAspectRatio="none" role="img" aria-label="Grasstreifen am unteren Rand">
      <defs>
        <linearGradient id="grassFill" x1="0" y1="0" x2="0" y2="1">
          <stop offset="0" stop-color="#7cc243"/>
          <stop offset="1" stop-color="#3f8f1f"/>
        </linearGradient>
      </defs>
      <rect x="0" y="14" width="580" height="56" fill="url(#grassFill)"/>
    </svg>
  </main>
</body>
</html>
```